Velmora Brightstead Website

Create website for Legal Management Company which specializes in Law Office Spersriinal Management
System implementation & Training
Global presence
Paralegal Services - Remote or In-Office
Legal Research
- Judge Motion Ruling History
- Opposing Counsel Opposition Research - Historical Filings - Pattern identification
Service by Mail - Ex- Parte Notice

Probate -Heir Finder - Asset Location -

```html
<!DOCTYPE html>
<html lang="en">
<head>
<meta charset="utf-8">
<title>Velmora Brightstead — Legal Management</title>
<link href="https://fonts.googleapis.com/css2?family=Marcellus&family=Nunito+Sans:wght@400;600;700&display=swap" rel="stylesheet">
<style>
:root{
  --navy:#1b3263;
  --navy-deep:#142754;
  --gold:#e2a221;
  --ink:#1e2c4c;
  --muted:#7b8396;
  --line:#e6e8ee;
  --paper:#ffffff;
  --mist:#f5f6f8;
  --stage:#b9babd;
}
*{box-sizing:border-box;margin:0;padding:0}
html,body{width:1200px;height:4474px;overflow:hidden}
body{background:var(--stage);font-family:"Nunito Sans",Arial,sans-serif;color:var(--ink);position:relative}
.page{position:absolute;left:83px;top:82px;width:1034px;height:4308px;background:var(--paper);overflow:hidden;box-shadow:0 4px 18px rgba(0,0,0,.25)}
.abs{position:absolute}
.serif{font-family:"Marcellus",Georgia,serif;font-weight:400;text-transform:uppercase;letter-spacing:.5px}
.gold{color:var(--gold)}
.btn{position:absolute;background:var(--gold);color:#fff;font-size:9px;font-weight:700;text-transform:uppercase;display:flex;align-items:center;justify-content:center;gap:6px;letter-spacing:.3px;white-space:nowrap}
.btn-outline{position:absolute;border:1px solid var(--navy);color:var(--navy);font-size:9px;font-weight:700;text-transform:uppercase;display:flex;align-items:center;justify-content:center;gap:6px;white-space:nowrap}
.photo{position:absolute}
.section-title{position:absolute;left:0;width:100%;text-align:center;font-size:24px;color:var(--navy)}
.title-rule{position:absolute;left:502px;width:30px;height:2px;background:var(--gold)}

/* hero */
.hero{position:absolute;left:0;top:0;width:1034px;height:535px;background:linear-gradient(100deg,#233d72 0%,#2a4780 45%,#1e3668 100%)}
.brand{position:absolute;left:142px;top:26px;display:flex;align-items:center;gap:8px;color:#fff}
.brand-mark{width:24px;height:24px;border-radius:50%;background:var(--gold);flex:none}
.brand-name{font-family:"Marcellus",Georgia,serif;font-size:13px;line-height:13px;text-transform:uppercase;width:100px}
.nav{position:absolute;left:325px;top:39px;display:flex;gap:19px;font-size:8.5px;font-weight:700;color:#fff;text-transform:uppercase;white-space:nowrap}
.call{position:absolute;left:785px;top:26px;color:#fff;white-space:nowrap}
.call small{display:block;font-size:7px;letter-spacing:.5px}
.call b{font-size:15px;font-weight:700}
.social{position:absolute;left:52px;width:24px;height:24px;border-radius:50%;border:1px solid rgba(255,255,255,.5);display:flex;align-items:center;justify-content:center}
.hero h1{position:absolute;left:217px;top:185px;color:#fff;font-size:44px;line-height:50px;white-space:nowrap}
.eyebrow{position:absolute;left:217px;top:158px;font-family:"Marcellus",Georgia,serif;font-size:12px;letter-spacing:3px;color:var(--gold);text-transform:uppercase}
.hero p{position:absolute;left:217px;top:293px;width:360px;font-size:12px;line-height:19px;color:#e3e8f3}

.svc{position:absolute;width:292px;height:114px;background:#fff;box-shadow:0 2px 10px rgba(20,39,84,.12);padding:22px 30px 0 54px}
.svc h3{font-size:12px;color:var(--navy);margin-bottom:6px;white-space:nowrap}
.svc p{font-size:8.5px;line-height:14px;color:var(--muted)}
.svc .ic{position:absolute;left:18px;top:22px}
.corner{position:absolute;right:0;bottom:0;width:34px;height:26px;background:var(--gold);border-top-left-radius:26px;display:flex;align-items:center;justify-content:center;padding-left:6px}

/* welcome */
.welcome-card{position:absolute;left:509px;top:785px;width:306px;height:361px;background:#fff;padding:40px 26px 0 26px}
.welcome-card h2{font-size:23px;line-height:32px;color:var(--navy);white-space:nowrap}
.welcome-card p{font-size:10px;line-height:16px;color:var(--muted);margin-top:16px}
.ticks{list-style:none;margin-top:8px}
.ticks li{font-size:9.5px;line-height:19px;color:var(--muted);display:flex;gap:8px;align-items:center;white-space:nowrap}
.cases{position:absolute;left:177px;top:1070px;width:127px;height:114px;background:var(--gold);color:#fff;text-align:center;padding-top:20px}
.cases b{font-family:"Marcellus",Georgia,serif;font-weight:400;font-size:36px;display:block;line-height:40px}
.cases span{font-size:11px;font-weight:700;line-height:13px;display:block}

/* experience */
.exp{position:absolute;left:0;top:1250px;width:1034px;height:443px;background:var(--navy)}
.stat{position:absolute;top:1426px;width:137px;height:85px;border:1px solid rgba(255,255,255,.18);background:rgba(20,39,84,.5);color:#fff;display:flex;align-items:center;gap:10px;padding-left:14px}
.stat b{font-family:"Marcellus",Georgia,serif;font-weight:400;font-size:20px;display:block}
.stat small{font-size:8.5px;color:#d9def0;white-space:nowrap}

/* practice */
.cell{position:absolute;width:149px;height:146px;text-align:center;padding-top:20px;border-right:1px solid var(--line);border-bottom:1px solid var(--line)}
.cell h4{font-size:10.5px;font-weight:400;color:var(--navy);text-transform:uppercase;margin-top:8px;white-space:nowrap}
.cell p{font-size:8.5px;line-height:13px;color:var(--muted);margin-top:6px}
.cell.active{background:var(--gold)}
.cell.active h4,.cell.active p{color:#fff}
.cell .arrow{margin-top:6px}

/* faq + form */
.faq{position:absolute;left:0;top:2339px;width:516px;height:450px;background:linear-gradient(120deg,#243f76,#1a3163)}
.faq h2{position:absolute;left:215px;top:76px;color:#fff;font-size:24px;line-height:32px}
.faq p.lead{position:absolute;left:215px;top:160px;width:260px;font-size:9.5px;line-height:16px;color:#dfe4f1}
.q{position:absolute;left:218px;width:256px;font-family:"Marcellus",Georgia,serif;font-size:10px;color:#fff;text-transform:uppercase;display:flex;justify-content:space-between;padding-bottom:8px;border-bottom:1px solid rgba(255,255,255,.25);white-space:nowrap}
.ans{position:absolute;left:218px;width:256px;font-size:8.5px;line-height:13px;color:#c5cde3}
.consult{position:absolute;left:516px;top:2339px;width:518px;height:450px;background:var(--mist)}
.consult h2{position:absolute;left:43px;top:76px;color:var(--navy);font-size:24px;line-height:32px}
.field{position:absolute;background:#fff;font-size:9px;color:var(--muted);padding:9px 10px}

/* team */
.member{position:absolute;top:2909px;width:137px;text-align:center}
.member .photo{position:static;width:137px;height:186px}
.member h5{font-size:11px;font-weight:400;color:var(--navy);text-transform:uppercase;margin-top:16px}
.member small{font-size:8.5px;color:var(--muted);display:block;margin-top:3px}

/* testimonial */
.testi{position:absolute;left:0;top:3218px;width:1034px;height:382px;background:var(--mist)}
.quote-card{position:absolute;left:283px;top:3391px;width:467px;height:115px;background:#fff;text-align:center;padding:32px 40px 0}
.quote-card p{font-size:10px;line-height:15px;color:var(--muted)}
.quote-card b{display:block;font-size:10px;font-weight:400;color:var(--gold);margin-top:6px;text-transform:uppercase}
.pager{position:absolute;top:3419px;width:38px;height:38px;border-radius:50%;display:flex;align-items:center;justify-content:center}

.partner{position:absolute;top:3767px;width:137px;height:52px;border:1px solid var(--line);display:flex;align-items:center;justify-content:center}

/* footer */
.footer{position:absolute;left:0;top:3972px;width:1034px;height:336px;background:var(--navy-deep)}
.cta-img{position:absolute;left:217px;top:3886px;width:271px;height:164px}
.cta-panel{position:absolute;left:488px;top:3886px;width:327px;height:164px;background:#fff;border-right:8px solid var(--gold);padding:40px 0 0 42px}
.cta-panel h2{font-size:22px;line-height:28px;color:var(--navy)}
.fcol{position:absolute;top:4143px;color:#fff}
.fcol h6{font-family:"Marcellus",Georgia,serif;font-weight:400;font-size:11px;text-transform:uppercase;margin-bottom:12px;letter-spacing:.5px}
.fcol li{list-style:none;font-size:8.5px;color:#b8c1d9;line-height:17px;white-space:nowrap}
.copy{position:absolute;left:0;width:100%;top:4283px;text-align:center;font-size:8px;color:#9aa6c4}
.rule-top{position:absolute;left:0;width:100%;height:1px;background:rgba(255,255,255,.12)}
</style>
</head>
<body>
<div class="page">

  <!-- HERO -->
  <section class="hero">
    <div class="photo" role="img" aria-label="Legal manager in a suit reviewing case files at a desk, toned in navy" style="left:120px;top:0;width:914px;height:535px;background:radial-gradient(ellipse at 70% 45%,rgba(70,96,150,.55),rgba(27,50,99,0) 65%)"></div>
    <div class="brand"><span class="brand-mark"></span><span class="brand-name">Velmora Brightstead</span></div>
    <nav class="nav"><span>Home</span><span>About Us</span><span>Our Services</span><span>Our Team</span><span>Blog</span></nav>
    <div class="btn" style="left:655px;top:30px;width:88px;height:27px">Contact Us</div>
    <svg class="abs" style="left:760px;top:28px" width="18" height="30" viewBox="0 0 18 30"><rect x="2" y="1" width="14" height="28" rx="2" fill="none" stroke="#fff" stroke-width="1.5"/><line x1="7" y1="25" x2="11" y2="25" stroke="#fff" stroke-width="1.5"/></svg>
    <div class="call"><small>CALL US TODAY!</small><b>+1 555 204 7719</b></div>
    <div class="social" style="top:217px"><svg width="8" height="8"><circle cx="4" cy="4" r="3" fill="#fff"/></svg></div>
    <div class="social" style="top:252px"><svg width="8" height="8"><circle cx="4" cy="4" r="3" fill="#fff"/></svg></div>
    <div class="social" style="top:288px"><svg width="8" height="8"><circle cx="4" cy="4" r="3" fill="#fff"/></svg></div>
    <div class="eyebrow">Legal Management —</div>
    <h1 class="serif">Law Office Support<br>Since 1968</h1>
    <p>Systems, paralegals, research and service of process for law offices, with a global presence and remote or in-office teams.</p>
    <div class="btn" style="left:217px;top:352px;width:137px;height:28px">Free Consultation →</div>
  </section>

  <!-- SERVICE CARDS -->
  <div class="svc" style="left:217px;top:476px">
    <svg class="ic" width="26" height="26" viewBox="0 0 26 26"><rect x="2" y="4" width="22" height="14" fill="none" stroke="#1b3263" stroke-width="1.4"/><path d="M9 22h8M13 18v4" stroke="#e2a221" stroke-width="1.4"/></svg>
    <h3 class="serif">System Implementation</h3>
    <p>Office management system setup and staff training, tailored to your firm's caseload and workflow.</p>
    <div class="corner"><svg width="10" height="8"><path d="M0 4h8M5 1l3 3-3 3" stroke="#fff" fill="none"/></svg></div>
  </div>
  <div class="svc" style="left:524px;top:476px">
    <svg class="ic" width="26" height="26" viewBox="0 0 26 26"><rect x="4" y="2" width="16" height="21" fill="none" stroke="#1b3263" stroke-width="1.4"/><path d="M8 8h8M8 12h8M8 16h5" stroke="#e2a221" stroke-width="1.4"/></svg>
    <h3 class="serif">Paralegal Services</h3>
    <p>Experienced paralegals working remote or in-office, ready to draft, file and manage your matters.</p>
    <div class="corner"><svg width="10" height="8"><path d="M0 4h8M5 1l3 3-3 3" stroke="#fff" fill="none"/></svg></div>
  </div>
  <div class="svc" style="left:217px;top:604px">
    <svg class="ic" width="26" height="26" viewBox="0 0 26 26"><circle cx="11" cy="11" r="7" fill="none" stroke="#1b3263" stroke-width="1.4"/><path d="M16 16l7 7" stroke="#e2a221" stroke-width="1.6"/></svg>
    <h3 class="serif">Legal Research</h3>
    <p>Judge motion ruling history and opposing counsel research, from past filings to clear patterns.</p>
    <div class="corner"><svg width="10" height="8"><path d="M0 4h8M5 1l3 3-3 3" stroke="#fff" fill="none"/></svg></div>
  </div>
  <div class="svc" style="left:524px;top:604px">
    <svg class="ic" width="26" height="26" viewBox="0 0 26 26"><circle cx="9" cy="9" r="4" fill="none" stroke="#1b3263" stroke-width="1.4"/><circle cx="18" cy="11" r="3" fill="none" stroke="#e2a221" stroke-width="1.4"/><path d="M2 22a7 7 0 0 1 14 0M14 22a5 5 0 0 1 10 0" fill="none" stroke="#1b3263" stroke-width="1.4"/></svg>
    <h3 class="serif">Probate Support</h3>
    <p>Heir finder and asset location services that help estates move forward with confidence.</p>
    <div class="corner"><svg width="10" height="8"><path d="M0 4h8M5 1l3 3-3 3" stroke="#fff" fill="none"/></svg></div>
  </div>

  <!-- WELCOME -->
  <div class="photo" role="img" aria-label="Legal manager in glasses reviewing a document with a client" style="left:217px;top:785px;width:292px;height:361px;background:linear-gradient(160deg,#d9dde3,#8d97a6 55%,#c7a27a)"></div>
  <div class="welcome-card">
    <h2 class="serif">Welcome to Your<br>Legal Back Office</h2>
    <p>We run the work behind the courtroom: management systems, paralegals, research and service, so your attorneys can focus on clients and results.</p>
    <ul class="ticks">
      <li><svg width="10" height="8"><path d="M1 4l3 3 5-6" stroke="#e2a221" fill="none" stroke-width="1.5"/></svg>System implementation and staff training.</li>
      <li><svg width="10" height="8"><path d="M1 4l3 3 5-6" stroke="#e2a221" fill="none" stroke-width="1.5"/></svg>Paralegal services, remote or in-office.</li>
      <li><svg width="10" height="8"><path d="M1 4l3 3 5-6" stroke="#e2a221" fill="none" stroke-width="1.5"/></svg>Service by mail and ex-parte notice.</li>
      <li><svg width="10" height="8"><path d="M1 4l3 3 5-6" stroke="#e2a221" fill="none" stroke-width="1.5"/></svg>Probate heir finder and asset location.</li>
    </ul>
  </div>
  <div class="btn" style="left:534px;top:1074px;width:101px;height:27px">Get a Quote →</div>
  <div class="btn-outline" style="left:647px;top:1074px;width:102px;height:27px">Read More →</div>
  <div class="cases"><b>1500<sup style="font-size:14px">+</sup></b><span>Matters<br>Supported</span></div>

  <!-- EXPERIENCE -->
  <section class="exp">
    <div class="photo" role="img" aria-label="Judge's gavel on a desk, toned in navy" style="left:0;top:60px;width:260px;height:300px;background:radial-gradient(ellipse at 30% 50%,rgba(120,110,70,.35),rgba(27,50,99,0) 70%)"></div>
    <div class="serif" style="position:absolute;left:0;width:100%;top:60px;text-align:center;color:#fff;font-size:23px">20 Years of Experience in Legal Management</div>
    <p style="position:absolute;left:0;width:100%;top:116px;text-align:center;color:#dfe4f1;font-size:11px;line-height:18px">Law offices around the world rely on our systems, paralegals and research teams<br>to keep filings on time and every matter moving forward</p>
  </section>
  <div class="stat" style="left:217px"><svg width="26" height="22"><rect x="1" y="5" width="24" height="16" fill="none" stroke="#e2a221" stroke-width="1.4"/><rect x="9" y="1" width="8" height="4" fill="none" stroke="#e2a221" stroke-width="1.4"/></svg><div><b>250<sup style="font-size:10px">+</sup></b><small>Law Offices Served</small></div></div>
  <div class="stat" style="left:370px"><svg width="26" height="22"><rect x="1" y="2" width="24" height="14" fill="none" stroke="#e2a221" stroke-width="1.4"/><path d="M8 21h10M13 16v5" stroke="#e2a221" stroke-width="1.4"/></svg><div><b>180<sup style="font-size:10px">+</sup></b><small>Systems Deployed</small></div></div>
  <div class="stat" style="left:524px"><svg width="26" height="22"><circle cx="13" cy="7" r="5" fill="none" stroke="#e2a221" stroke-width="1.4"/><path d="M3 21a10 7 0 0 1 20 0" fill="none" stroke="#e2a221" stroke-width="1.4"/></svg><div><b>350<sup style="font-size:10px">+</sup></b><small>Heirs Located</small></div></div>
  <div class="stat" style="left:678px"><svg width="26" height="22"><circle cx="13" cy="11" r="9" fill="none" stroke="#e2a221" stroke-width="1.4"/><path d="M4 11h18M13 2c-4 5-4 13 0 18M13 2c4 5 4 13 0 18" fill="none" stroke="#e2a221" stroke-width="1.2"/></svg><div><b>15<sup style="font-size:10px">+</sup></b><small>Countries Served</small></div></div>
  <div class="photo" role="img" aria-label="Overhead view of paralegals and attorneys meeting around a wooden table" style="left:217px;top:1547px;width:598px;height:313px;background:linear-gradient(135deg,#d8dbe0 0%,#b58a5e 40%,#a67a4f 60%,#3a4356 100%)"></div>
  <svg class="abs" style="left:484px;top:1672px" width="64" height="64"><circle cx="32" cy="32" r="31" fill="#fff"/><path d="M27 22v20l15-10z" fill="#1b3263"/></svg>

  <!-- SERVICE AREAS -->
  <h2 class="section-title serif" style="top:1920px">Our Legal Management Services</h2>
  <div class="title-rule" style="top:1956px"></div>
  <div class="cell" style="left:217px;top:1980px"><svg width="28" height="26"><rect x="3" y="3" width="22" height="15" fill="none" stroke="#1b3263" stroke-width="1.4"/><path d="M10 23h8M14 18v5" stroke="#e2a221" stroke-width="1.4"/></svg><h4>System Setup</h4><p>Office management system<br>implementation</p><div class="arrow"><svg width="10" height="8"><path d="M0 4h8M5 1l3 3-3 3" stroke="#e2a221" fill="none"/></svg></div></div>
  <div class="cell active" style="left:366px;top:1980px"><svg width="28" height="26"><rect x="3" y="7" width="22" height="17" fill="none" stroke="#fff" stroke-width="1.4"/><rect x="10" y="2" width="8" height="5" fill="none" stroke="#fff" stroke-width="1.4"/><path d="M3 14h22" stroke="#fff" stroke-width="1.4"/></svg><h4>Paralegal Services</h4><p>Remote or in-office staff<br>for daily casework</p><div class="arrow"><svg width="10" height="8"><path d="M0 4h8M5 1l3 3-3 3" stroke="#fff" fill="none"/></svg></div></div>
  <div class="cell" style="left:515px;top:1980px"><svg width="28" height="26"><circle cx="11" cy="10" r="7" fill="none" stroke="#1b3263" stroke-width="1.4"/><path d="M16 15l7 7" stroke="#e2a221" stroke-width="1.6"/></svg><h4>Judge Ruling History</h4><p>Motion ruling records<br>for every judge</p><div class="arrow"><svg width="10" height="8"><path d="M0 4h8M5 1l3 3-3 3" stroke="#e2a221" fill="none"/></svg></div></div>
  <div class="cell" style="left:664px;top:1980px;border-right:none"><svg width="28" height="26"><circle cx="10" cy="8" r="5" fill="none" stroke="#1b3263" stroke-width="1.4"/><path d="M2 24a8 8 0 0 1 16 0" fill="none" stroke="#1b3263" stroke-width="1.4"/><path d="M19 10h7M19 14h7M19 18h5" stroke="#e2a221" stroke-width="1.4"/></svg><h4>Counsel Research</h4><p>Historical filings and<br>pattern identification</p><div class="arrow"><svg width="10" height="8"><path d="M0 4h8M5 1l3 3-3 3" stroke="#e2a221" fill="none"/></svg></div></div>
  <div class="cell" style="left:217px;top:2126px;border-bottom:none"><svg width="28" height="26"><circle cx="14" cy="7" r="5" fill="none" stroke="#1b3263" stroke-width="1.4"/><path d="M4 25a10 9 0 0 1 20 0" fill="none" stroke="#1b3263" stroke-width="1.4"/><path d="M12 17h4M14 15v4" stroke="#e2a221" stroke-width="1.4"/></svg><h4>Staff Training</h4><p>Hands-on training for<br>attorneys and staff</p><div class="arrow"><svg width="10" height="8"><path d="M0 4h8M5 1l3 3-3 3" stroke="#e2a221" fill="none"/></svg></div></div>
  <div class="cell" style="left:366px;top:2126px;border-bottom:none"><svg width="28" height="26"><rect x="3" y="6" width="22" height="15" fill="none" stroke="#1b3263" stroke-width="1.4"/><path d="M3 6l11 8 11-8" fill="none" stroke="#e2a221" stroke-width="1.4"/></svg><h4>Service by Mail</h4><p>Documents served and<br>proof of service filed</p><div class="arrow"><svg width="10" height="8"><path d="M0 4h8M5 1l3 3-3 3" stroke="#e2a221" fill="none"/></svg></div></div>
  <div class="cell" style="left:515px;top:2126px;border-bottom:none"><svg width="28" height="26"><path d="M14 2v22M4 6h20M9 24h10" fill="none" stroke="#1b3263" stroke-width="1.4"/><path d="M4 6l-3 8h6zM24 6l-3 8h6z" fill="none" stroke="#e2a221" stroke-width="1.4"/></svg><h4>Ex-Parte Notice</h4><p>Timely notice prepared<br>and delivered</p><div class="arrow"><svg width="10" height="8"><path d="M0 4h8M5 1l3 3-3 3" stroke="#e2a221" fill="none"/></svg></div></div>
  <div class="cell" style="left:664px;top:2126px;border:none"><svg width="28" height="26"><rect x="6" y="2" width="16" height="22" fill="none" stroke="#1b3263" stroke-width="1.4"/><path d="M10 8h8M10 12h8M10 16h5" stroke="#e2a221" stroke-width="1.4"/></svg><h4>Heir &amp; Asset Finder</h4><p>Probate heir search and<br>asset location</p><div class="arrow"><svg width="10" height="8"><path d="M0 4h8M5 1l3 3-3 3" stroke="#e2a221" fill="none"/></svg></div></div>

  <!-- FAQ -->
  <section class="faq">
    <h2 class="serif">Frequently Asked<br>Questions</h2>
    <p class="lead">Answers on how we work with law offices, from system rollout and training to paralegal staffing, research and probate support.</p>
    <div class="q" style="top:225px"><span>Do you offer remote paralegals?</span><span>+</span></div>
    <div class="q" style="top:268px;border-bottom:none"><span>How is service by mail handled?</span><span>–</span></div>
    <div class="ans" style="top:288px">We prepare and mail each document, track delivery and file proof of service, including ex-parte notice when deadlines are tight.</div>
    <div class="q" style="top:360px"><span>Can you locate heirs and assets?</span><span>+</span></div>
  </section>
  <section class="consult">
    <h2 class="serif">Get a Free<br>Consultation</h2>
    <div class="field" style="left:43px;top:153px;width:123px;height:28px">Name</div>
    <div class="field" style="left:176px;top:153px;width:124px;height:28px">Phone</div>
    <div class="field" style="left:43px;top:195px;width:257px;height:28px;display:flex;justify-content:space-between">Service Needed<span>⌄</span></div>
    <div class="field" style="left:43px;top:235px;width:257px;height:100px">Message</div>
    <div class="btn" style="left:43px;top:354px;width:103px;height:25px">Submit Now →</div>
    <div class="photo" role="img" aria-label="Faint decorative open book with a fountain pen nib" style="left:370px;top:250px;width:130px;height:110px;background:radial-gradient(ellipse at 50% 60%,rgba(226,162,33,.18),rgba(226,162,33,0) 70%)"></div>
  </section>

  <!-- TEAM -->
  <h2 class="section-title serif" style="top:2849px">Our Professional Team</h2>
  <div class="title-rule" style="top:2885px"></div>
  <div class="member" style="left:217px"><div class="photo" role="img" aria-label="Portrait of the founder in a dark suit" style="background:linear-gradient(180deg,#d4d6d9,#2b2f38)"></div><h5>Daniel Moreau</h5><small>Founder and CEO</small><svg style="margin-top:6px" width="10" height="8"><path d="M0 4h8M5 1l3 3-3 3" stroke="#e2a221" fill="none"/></svg></div>
  <div class="member" style="left:370px"><div class="photo" role="img" aria-label="Portrait of the paralegal lead in a dark blazer" style="background:linear-gradient(180deg,#dcdddf,#3a3c42)"></div><h5>Sara Lindqvist</h5><small>Paralegal Lead</small><svg style="margin-top:6px" width="10" height="8"><path d="M0 4h8M5 1l3 3-3 3" stroke="#e2a221" fill="none"/></svg></div>
  <div class="member" style="left:524px"><div class="photo" role="img" aria-label="Portrait of a research analyst with arms crossed" style="background:linear-gradient(180deg,#d9dadc,#33353b)"></div><h5>Ivy Harlow</h5><small>Research Analyst</small><svg style="margin-top:6px" width="10" height="8"><path d="M0 4h8M5 1l3 3-3 3" stroke="#e2a221" fill="none"/></svg></div>
  <div class="member" style="left:678px"><div class="photo" role="img" aria-label="Portrait of a probate specialist in a dark suit" style="background:linear-gradient(180deg,#dadbdd,#2a2c31)"></div><h5>Marcus Hale</h5><small>Probate Specialist</small><svg style="margin-top:6px" width="10" height="8"><path d="M0 4h8M5 1l3 3-3 3" stroke="#e2a221" fill="none"/></svg></div>

  <!-- TESTIMONIALS -->
  <section class="testi">
    <h2 class="section-title serif" style="top:60px">What Our Clients Said</h2>
  </section>
  <div class="photo" role="img" aria-label="Client portrait avatar" style="left:490px;top:3343px;width:52px;height:52px;border-radius:50%;background:linear-gradient(180deg,#cfd3d8,#6e7480);border:3px solid #fff"></div>
  <div class="quote-card">
    <div class="gold serif" style="position:absolute;left:28px;top:14px;font-size:28px">“</div>
    <p>Their new system and remote paralegals cut our filing delays in half, and the judge ruling history gave us a real edge before every motion hearing.</p>
    <b>Owen Castell</b>
  </div>
  <div class="pager" style="left:219px;background:var(--navy)"><svg width="12" height="10"><path d="M11 5H2M5 1L1 5l4 4" stroke="#fff" fill="none" stroke-width="1.4"/></svg></div>
  <div class="pager" style="left:775px;background:var(--gold)"><svg width="12" height="10"><path d="M1 5h9M7 1l4 4-4 4" stroke="#fff" fill="none" stroke-width="1.4"/></svg></div>
  <svg class="abs" style="left:496px;top:3523px" width="42" height="10"><circle cx="5" cy="5" r="4" fill="#f0d9a6"/><circle cx="21" cy="5" r="4" fill="#e2a221"/><circle cx="37" cy="5" r="4" fill="#f0d9a6"/></svg>

  <!-- PARTNERS -->
  <h2 class="section-title serif" style="top:3659px">Trusted Companies</h2>
  <p style="position:absolute;left:0;width:100%;top:3716px;text-align:center;font-size:10px;line-height:16px;color:var(--muted)">Law offices and legal departments across several continents trust us with their systems,<br>staffing, research and service of process</p>
  <div class="partner" style="left:217px"><svg width="70" height="18"><rect x="0" y="0" width="70" height="18" rx="3" fill="#e4e6ea"/></svg></div>
  <div class="partner" style="left:370px"><svg width="70" height="18"><rect x="0" y="0" width="70" height="18" rx="3" fill="#f2ddb0"/></svg></div>
  <div class="partner" style="left:524px"><svg width="40" height="28"><circle cx="20" cy="14" r="13" fill="#e4e6ea"/></svg></div>
  <div class="partner" style="left:678px"><svg width="70" height="18"><rect x="0" y="0" width="70" height="18" rx="3" fill="#e4e6ea"/></svg></div>

  <!-- FOOTER -->
  <footer class="footer">
    <div class="brand" style="top:172px;left:217px"><span class="brand-mark"></span><span class="brand-name">Velmora Brightstead</span></div>
    <p style="position:absolute;left:217px;top:216px;width:180px;font-size:8.5px;line-height:15px;color:#b8c1d9">Legal management, paralegal services and research for law offices, remote or in-office, worldwide.</p>
    <svg class="abs" style="left:217px;top:276px" width="80" height="14"><circle cx="7" cy="7" r="4" fill="#fff"/><circle cx="38" cy="7" r="4" fill="#fff"/><circle cx="69" cy="7" r="4" fill="#fff"/></svg>
    <div class="rule-top" style="top:298px"></div>
  </footer>
  <div class="cta-img photo" role="img" aria-label="Legal manager working on a laptop in an office" style="background:linear-gradient(120deg,#c9ccd1,#5d6778 55%,#303848)"></div>
  <div class="cta-panel">
    <h2 class="serif">Speak With Our<br>Experts Today!</h2>
    <div class="btn" style="left:42px;top:112px;width:101px;height:25px">Contact Us →</div>
  </div>
  <div class="photo" role="img" aria-label="Wooden judge's gavel" style="left:760px;top:3870px;width:200px;height:200px;background:linear-gradient(135deg,rgba(60,32,20,0) 20%,rgba(60,32,20,.7) 45%,rgba(90,50,30,.55) 60%,rgba(60,32,20,0) 80%)"></div>
  <div class="fcol" style="left:420px"><h6>Useful Links</h6><ul><li>› Home</li><li>› About Us</li><li>› Our Services</li><li>› Legal Research</li><li>› Blog</li><li>› Contact Us</li></ul></div>
  <div class="fcol" style="left:530px"><h6>Office Info</h6><ul><li>☏ +1 555 204 7719</li><li>✉ hello@velmoralegal.com</li><li style="line-height:14px;margin-top:4px">⌖ 48 Harrow Lane Eastbrook,<br>&nbsp;&nbsp;&nbsp;2040</li></ul></div>
  <div class="fcol" style="left:677px"><h6>Subscribe Now</h6>
    <div style="width:137px;height:24px;border:1px solid rgba(255,255,255,.25);font-size:8px;color:#b8c1d9;padding:7px 8px">Enter Email Address</div>
    <div class="btn" style="position:relative;margin-top:10px;width:137px;height:24px">Subscribe Now →</div>
  </div>
  <div class="copy">Copyright 2021, Velmora Brightstead. All Rights Reserved.</div>

</div>
</body>
</html>
```